Custom open/closed sign for our young jewellery and silk shop

We are a new jewellery and silk store in Wellington, New Zealand specialising in products sourced from Suzhou, China.

We're after a design for an open/closed sign for our door. I know it sounds odd, but we want to put a bit of effort into making it special.

We've been thinking about designs relating to round Chinese garden moon gates with doors, to match with our round logo in some way, but are open to other ideas.

Our font is Avenir, so try to work with that if you can.

Have attached our logos on black/white for reference.

Target Market(s)

People gazing at our door - people in a hurry, people who don't know who we are, etc

Industry/Entity Type

Jewelry Store

Font styles to use
Other font styles liked:
• Avenir Pro

Colors
fece3e
ffffff
000000

Requirements
Must have
• The words "open" and "closed" on each side, possibly with "We are" or "Sorry we're" or something similar.
• Needs to fit within a 300mm square area, but if it's rectangular, aim for a 300x130mm kind of size.
• Writing should be in Avenir and letter spaced similarly to our logo.
Nice to have
• We like the idea of Chinese moon gate (https://en.brollapedia.net/wiki/Ring_door) to fit with our overall Chinese/oriental theme.
• On a black background is probably preferred, but not essential.
Should not have
• Colours that vastly don't match our black/white/yellow theme.

```html
<!DOCTYPE html>
<html lang="en">
<head>
<meta charset="utf-8">
<title>Lingxi Gallery — Open / Closed Door Sign</title>
<link rel="stylesheet" href="https://fonts.googleapis.com/css2?family=Nunito+Sans:wght@300;400&family=Noto+Sans+SC:wght@400&display=swap">
<style>
  :root {
    --page: #ffffff;
    --sign: #2f2f30;
    --roof-dark: #1c1c1c;
    --roof-light: #3a3a3a;
    --frame: #57524d;
    --gold: #f4b24c;
    --white: #ffffff;
    --door-red: #c4502c;
    --door-deep: #7a2a16;
    --room-light: #b9c2c0;
    --room-dark: #3b3d3d;
  }
  html, body {
    margin: 0;
    width: 1200px;
    height: 900px;
    overflow: hidden;
    background: var(--page);
  }
  .canvas {
    position: relative;
    width: 1200px;
    height: 900px;
  }
  .door-sign {
    position: absolute;
    left: 136px;
    width: 940px;
    height: 406px;
    display: block;
  }
  .door-sign--closed { top: 32px; }
  .door-sign--open { top: 462px; }
  .sign-body { fill: var(--sign); }
  .gate-frame { fill: var(--frame); }
  .status-ring { fill: none; stroke: var(--gold); stroke-width: 2.5; }
  .status-glyph {
    font-family: "Noto Sans SC", sans-serif;
    font-size: 64px;
    fill: var(--gold);
  }
  .status-word {
    font-family: "Nunito Sans", sans-serif;
    font-weight: 300;
    font-size: 60px;
    fill: var(--white);
  }
  .status-rule { stroke: var(--white); stroke-width: 3; }
  .info-label {
    font-family: "Nunito Sans", sans-serif;
    font-weight: 400;
    font-size: 15px;
    fill: var(--gold);
  }
  .info-text {
    font-family: "Nunito Sans", sans-serif;
    font-weight: 400;
    font-size: 15px;
    fill: var(--white);
  }
  .brand-mark { fill: none; stroke: var(--gold); stroke-width: 1.5; }
  .brand-name {
    font-family: "Nunito Sans", sans-serif;
    font-weight: 400;
    font-size: 15px;
    fill: var(--gold);
  }
</style>
</head>
<body>
<main class="canvas">

  <svg class="door-sign door-sign--closed" viewBox="0 0 940 406" aria-label="Closed sign">
    <defs>
      <linearGradient id="roof-tiles" x1="0" y1="0" x2="0" y2="1">
        <stop offset="0" stop-color="var(--roof-light)"/>
        <stop offset="1" stop-color="var(--roof-dark)"/>
      </linearGradient>
      <radialGradient id="red-door" cx="0.5" cy="0.4" r="0.65">
        <stop offset="0" stop-color="var(--door-red)"/>
        <stop offset="1" stop-color="var(--door-deep)"/>
      </radialGradient>
    </defs>
    <rect class="sign-body" width="940" height="406"/>
    <rect class="roof-band" width="940" height="53" fill="url(#roof-tiles)" role="img" aria-label="Band of dark Chinese roof tiles"/>
    <path class="gate-frame" d="M134 406 L134 375.8 A172 172 0 1 1 310 375.8 L310 406 Z"/>
    <path class="gate-opening" d="M150 406 L150 364.1 A154 154 0 1 1 294 364.1 L294 406 Z" fill="url(#red-door)" role="img" aria-label="Weathered red double doors with brass knockers inside a moon gate"/>

    <circle class="status-ring" cx="533" cy="136" r="70"/>
    <text class="status-glyph" x="533" y="162" text-anchor="middle">关</text>
    <text class="status-word" x="451" y="236" textLength="410" lengthAdjust="spacing">CLOSED</text>
    <line class="status-rule" x1="451" y1="260" x2="857" y2="260"/>

    <text class="info-label" x="451" y="293">OPENING HOURS</text>
    <text class="info-label" x="857" y="293" text-anchor="end">(04) 555 0182</text>
    <text class="info-text" x="451" y="328">Monday – Friday</text>
    <text class="info-text" x="585" y="328">9:30am – 5pm</text>
    <text class="info-text" x="451" y="345">Saturday &amp; Sunday</text>
    <text class="info-text" x="585" y="345">10am – 4pm</text>
    <text class="info-text" x="451" y="380">We're open most public holidays from 10am – 4pm</text>

    <circle class="brand-mark" cx="780" cy="104" r="7"/>
    <text class="brand-name" x="916" y="109" text-anchor="end">Lingxi Gallery</text>
  </svg>

  <svg class="door-sign door-sign--open" viewBox="0 0 940 406" aria-label="Open sign">
    <defs>
      <linearGradient id="roof-tiles-open" x1="0" y1="0" x2="0" y2="1">
        <stop offset="0" stop-color="var(--roof-light)"/>
        <stop offset="1" stop-color="var(--roof-dark)"/>
      </linearGradient>
      <linearGradient id="gallery-room" x1="0" y1="0" x2="0.3" y2="1">
        <stop offset="0" stop-color="var(--room-light)"/>
        <stop offset="0.55" stop-color="#7c8584"/>
        <stop offset="1" stop-color="var(--room-dark)"/>
      </linearGradient>
    </defs>
    <rect class="sign-body" width="940" height="406"/>
    <rect class="roof-band" width="940" height="53" fill="url(#roof-tiles-open)" role="img" aria-label="Band of dark Chinese roof tiles"/>
    <path class="gate-frame" d="M134 406 L134 375.8 A172 172 0 1 1 310 375.8 L310 406 Z"/>
    <path class="gate-opening" d="M150 406 L150 364.1 A154 154 0 1 1 294 364.1 L294 406 Z" fill="url(#gallery-room)" role="img" aria-label="View through a moon gate into the gallery with glass jewellery display cases"/>

    <circle class="status-ring" cx="533" cy="136" r="70"/>
    <text class="status-glyph" x="533" y="162" text-anchor="middle">开</text>
    <text class="status-word" x="451" y="236" textLength="270" lengthAdjust="spacing">OPEN</text>
    <line class="status-rule" x1="451" y1="260" x2="857" y2="260"/>

    <text class="info-label" x="451" y="293">OPENING HOURS</text>
    <text class="info-label" x="857" y="293" text-anchor="end">(04) 555 0182</text>
    <text class="info-text" x="451" y="328">Monday – Friday</text>
    <text class="info-text" x="585" y="328">9:30am – 5pm</text>
    <text class="info-text" x="451" y="345">Saturday &amp; Sunday</text>
    <text class="info-text" x="585" y="345">10am – 4pm</text>
    <text class="info-text" x="451" y="380">We're open most public holidays from 10am – 4pm</text>

    <circle class="brand-mark" cx="780" cy="104" r="7"/>
    <text class="brand-name" x="916" y="109" text-anchor="end">Lingxi Gallery</text>
  </svg>

</main>
</body>
</html>
```